依頼詳細
ポスティングを予定しております。顧客の目に留まりやすい、問い合わせをしたくなるようなチラシをお願いさせて頂きます。

メニューは日替わり弁当だけです。
記載項目
社名:青葉デリカフーズ株式会社
住所:横浜市磯子区松葉台312
電話:045-762-3904
FAX:045-762-3909
2次元バーコード添付
サイズ
B5
ページ数
片面
希望イメージ
シンプル 複雑
単色 カラフル
暗い 明るい
日常 高級
遊び心 厳粛
未来的 伝統的
女性的 男性的
希望する色
設定なし
納品ファイル
設定なし
補足説明
初めてですので、右も左も分からない状態です。
できる限りのことは致しますので、どうぞよろしくお願い致します。

頭の中のイメージと一番近かった。

提案してくださったランサーの皆様、本当のどうもありがとうございました。
ビックリするほど沢山の提案があり本当に悩みました。

初めての依頼ということで、いろいろと不備があったと思いますが
ご尽力いただき深く感謝いたします。

また何かご縁がありましたら、
どうぞ宜しくお願い致します。

```html
<!DOCTYPE html>
<html lang="ja">
<head>
<meta charset="utf-8">
<title>日替りランチ弁当 チラシ</title>
<link href="https://fonts.googleapis.com/css2?family=Noto+Sans+JP:wght@400;500;700;900&display=swap" rel="stylesheet">
<style>
:root{
  --red:#e4151b;
  --deep-red:#c20d12;
  --orange:#ef7d12;
  --ink:#333333;
  --paper:#ffffff;
  --cream:#fff7d6;
  --skyline:#f3eeee;
}
*{box-sizing:border-box;margin:0;padding:0}
html,body{width:849px;height:1200px;overflow:hidden;background:var(--paper)}
body{font-family:"Noto Sans JP",sans-serif;color:var(--ink)}
.flyer{position:relative;width:849px;height:1200px;overflow:hidden;background:var(--paper)}

.skyline{position:absolute;left:0;top:150px;width:849px;height:200px;
  background:linear-gradient(180deg,rgba(243,238,238,0) 0%,var(--skyline) 100%)}

.tagline{position:absolute;left:34px;top:22px;font-size:37px;font-weight:900;letter-spacing:1px;line-height:1}
.tagline .lead{color:var(--orange)}
.tagline .rest{color:var(--red)}

.badge{position:absolute;left:34px;top:100px;width:170px;height:170px}
.badge-text{position:absolute;left:34px;top:100px;width:170px;height:160px;display:flex;align-items:center;justify-content:center;
  writing-mode:vertical-rl;font-size:48px;font-weight:900;color:var(--red);letter-spacing:2px}

.headline{position:absolute;left:212px;top:92px;color:var(--red);font-weight:900;line-height:1.12;font-size:96px;letter-spacing:-1px}
.headline span{display:block}
.headline .line2{padding-left:0}

.rule{position:absolute;left:34px;top:345px;width:781px;height:4px;background:var(--red)}

.question{position:absolute;left:34px;top:366px;font-size:33px;font-weight:900;color:var(--red);letter-spacing:.5px}

.intro{position:absolute;left:34px;top:420px;width:600px;font-size:15px;font-weight:500;line-height:1.75;color:var(--ink)}

.van{position:absolute;left:660px;top:410px;width:150px;height:90px}

.photos{position:absolute;left:28px;top:520px;width:793px;height:440px;border:4px solid var(--red);background:var(--red);display:grid;grid-template-columns:497px 1fr;grid-template-rows:1fr 1fr;gap:4px}
.photo{width:100%;height:100%}
.photo-main{grid-row:1 / 3;background:radial-gradient(ellipse at 45% 45%,#b5673a 0%,#8a4a2a 40%,#3f2a1e 100%)}
.photo-side-a{background:radial-gradient(ellipse at 50% 55%,#d99a4e 0%,#b7702f 45%,#5a3b25 100%)}
.photo-side-b{background:radial-gradient(ellipse at 50% 50%,#e9c067 0%,#c78a3e 45%,#6b4328 100%)}

.price{position:absolute;left:28px;top:985px;display:flex;align-items:flex-end;color:var(--red)}
.price-label{font-size:34px;font-weight:900;line-height:1.1;color:var(--ink);margin-right:14px;margin-bottom:6px}
.price-num{font-size:108px;font-weight:900;line-height:.9;letter-spacing:-2px}
.price-unit{font-size:40px;font-weight:900;margin-left:4px;margin-bottom:4px}
.price-tax{font-size:16px;font-weight:700;writing-mode:vertical-rl;margin-left:2px;margin-bottom:10px}

.notes{position:absolute;left:430px;top:985px;width:390px;list-style:none;font-size:13px;line-height:1.85;color:var(--ink)}

.note-delivery{position:absolute;left:0;top:1092px;width:849px;text-align:center;font-size:24px;font-weight:900;color:var(--red)}

.footer{position:absolute;left:0;top:1132px;width:849px;height:68px;border-top:3px solid var(--red)}
.service{position:absolute;left:28px;top:7px;width:118px;height:32px;background:var(--red);color:var(--paper);font-size:11px;font-weight:700;line-height:1.3;text-align:center;padding-top:2px}
.company{position:absolute;left:156px;top:3px;font-size:27px;font-weight:900;color:var(--deep-red);letter-spacing:1px}
.address{position:absolute;left:570px;top:9px;font-size:12px;font-weight:500;line-height:1.35;color:var(--ink)}
.order{position:absolute;left:28px;top:42px;width:118px;height:22px;background:var(--red);color:var(--paper);font-size:12px;font-weight:700;text-align:center;line-height:22px}
.contact{position:absolute;top:36px;display:flex;align-items:center;font-weight:900;color:var(--red);font-size:28px;line-height:1}
.contact.tel{left:156px}
.contact.fax{left:406px}
.contact svg{width:26px;height:26px;margin-right:6px}
.contact .tag{font-size:13px;font-weight:900;background:var(--red);color:var(--paper);padding:2px 4px;margin-right:6px}
</style>
</head>
<body>
<main class="flyer">
  <div class="skyline" role="img" aria-label="淡い街並みのシルエット"></div>

  <p class="tagline"><span class="lead">新鮮で美味しく、</span><span class="rest">健康にこだわった手作りの味!</span></p>

  <svg class="badge" viewBox="0 0 170 170" aria-hidden="true">
    <path d="M85 8 C130 8 160 38 160 80 C160 122 130 150 85 150 C74 150 64 148 55 144 L28 162 L36 134 C18 120 10 102 10 80 C10 38 40 8 85 8 Z" fill="var(--cream)" stroke="var(--red)" stroke-width="6"/>
  </svg>
  <div class="badge-text">日替り</div>

  <h1 class="headline"><span class="line1">ランチ弁当を</span><span class="line2">お届けします!</span></h1>

  <div class="rule"></div>

  <h2 class="question">お昼は毎日コンビニのお弁当を食べていませんか?</h2>

  <p class="intro">毎日コンビニのお弁当ばかりでは栄養が偏りがちです。当店では野菜をたっぷり使い、塩分と油を控えた手作りのおかずを毎日日替わりでご用意しています。地元横浜で長年愛される味を、職場までできたてでお届けします。</p>

  <div class="van" role="img" aria-label="配達用の赤いワゴン車のイラスト">
    <svg viewBox="0 0 150 90" width="150" height="90" aria-hidden="true">
      <rect x="4" y="10" width="142" height="64" rx="10" fill="var(--red)"/>
    </svg>
  </div>

  <section class="photos">
    <div class="photo photo-main" role="img" aria-label="ハンバーグ、焼きそば、煮物が入った日替り弁当の写真"></div>
    <div class="photo photo-side-a" role="img" aria-label="揚げ物とサラダの日替り弁当の写真"></div>
    <div class="photo photo-side-b" role="img" aria-label="オムレツと惣菜の日替り弁当の写真"></div>
  </section>

  <div class="price">
    <div class="price-label">日替り<br>弁　当</div>
    <div class="price-num">000</div>
    <div class="price-unit">円</div>
    <div class="price-tax">(税込)</div>
  </div>

  <ul class="notes">
    <li>※前日の午後3時までにご注文ください。</li>
    <li>※5個以上のご注文から配達いたします。</li>
    <li>※土曜・日曜・祝日はお休みをいただきます。</li>
    <li>※配達エリアは横浜市内が中心となります。</li>
  </ul>

  <p class="note-delivery">※企業様以外にも、工事現場等にも配達可能です。</p>

  <footer class="footer">
    <div class="service">企業向け弁当<br>製造・配送販売</div>
    <div class="company">青葉デリカフーズ株式会社</div>
    <div class="address">〒235-0000<br>横浜市磯子区松葉台312</div>
    <div class="order">ご注文はコチラ</div>
    <div class="contact tel">
      <svg viewBox="0 0 24 24" aria-hidden="true"><path fill="var(--red)" d="M6.6 10.8a15.1 15.1 0 0 0 6.6 6.6l2.2-2.2c.3-.3.7-.4 1-.2 1.1.4 2.3.6 3.6.6.6 0 1 .4 1 1V20c0 .6-.4 1-1 1C10.6 21 3 13.4 3 4c0-.6.4-1 1-1h3.5c.6 0 1 .4 1 1 0 1.3.2 2.5.6 3.6.1.3 0 .7-.2 1z"/></svg>
      045-762-3904
    </div>
    <div class="contact fax"><span class="tag">FAX</span>045-762-3909</div>
  </footer>
</main>
</body>
</html>
```